Ferncrest Dental, LLC business card project

Business card to be designed with current logo.
Dental office- please keep design of card that looks clean and professional.
Please include the following info:
Ferncrest Dental, LLC
Dr. Lorna Pettigrew
2871 Marlowe Street
Bethlehem, PA 18093
610-555-0193
ferncrestdental.office@examplemail.test
Hello everyone-
Reason: Just got back from overseas- will look at all designs and provide feedback. Thank you!
Reason: Polling my friends for the final selection-
thank you to all those that participated- so many talented designers!

```html
<!DOCTYPE html>
<html lang="en">
<head>
<meta charset="utf-8">
<title>Ferncrest Dental, LLC – Business Card</title>
<link rel="stylesheet" href="https://fonts.googleapis.com/css2?family=Exo+2:wght@300;400;500&display=swap">
<style>
  :root {
    --page-bg: #f4f4f5;
    --card-green: #8dc63f;
    --card-dark-1: #3a3a3c;
    --card-dark-2: #111112;
    --accent-blue: #29abe2;
    --ink-light: #ffffff;
    --card-shadow: 0 2px 6px rgba(0,0,0,0.25);
  }
  * { margin: 0; padding: 0; box-sizing: border-box; }
  html, body {
    width: 1200px; height: 1000px; overflow: hidden;
    background: var(--page-bg);
    font-family: "Exo 2", sans-serif;
  }
  .card {
    position: absolute;
    top: 350px;
    width: 525px; height: 300px;
    box-shadow: var(--card-shadow);
    overflow: hidden;
    color: var(--ink-light);
  }

  /* Front */
  .card-front { left: 60px; background: var(--card-green); }
  .brand-dot {
    position: absolute; left: 40px; top: 30px;
    width: 34px; height: 34px; border-radius: 50%;
    background: var(--ink-light);
  }
  .front-brand {
    position: absolute; left: 23px; top: 110px;
    font-size: 24px; font-weight: 300; letter-spacing: -0.3px;
  }
  .front-rule {
    position: absolute; left: 22px; top: 142px;
    width: 236px; height: 2px; background: var(--ink-light);
  }
  .front-doctor {
    position: absolute; left: 24px; top: 147px;
    font-size: 22px; font-weight: 500;
  }
  .contact-list {
    position: absolute; left: 24px; top: 210px;
    list-style: none; font-size: 13px; font-weight: 400; line-height: 16px;
  }
  .contact-list li { display: flex; align-items: flex-start; margin-bottom: 5px; }
  .contact-list svg { width: 18px; height: 14px; margin-right: 6px; flex: none; margin-top: 1px; }

  /* Back */
  .card-back {
    left: 614px;
    background: linear-gradient(135deg, var(--card-dark-1) 0%, var(--card-dark-2) 70%);
  }
  .back-brand {
    position: absolute; left: 0; right: 0; top: 128px;
    display: flex; align-items: center; justify-content: center; gap: 14px;
  }
  .back-brand .brand-mark {
    width: 30px; height: 30px; border-radius: 50%; background: var(--ink-light);
  }
  .back-brand .brand-name { font-size: 38px; font-weight: 300; letter-spacing: -0.5px; }
  .back-band { position: absolute; left: 0; bottom: 0; width: 525px; height: 36px; }
  .back-doctor {
    position: absolute; left: 0; right: 0; bottom: 7px;
    text-align: center; font-size: 17px; font-weight: 500;
  }
</style>
</head>
<body>

<section class="card card-front" aria-label="Business card front">
  <div class="brand-dot"></div>
  <div class="front-brand">Ferncrest Dental, LLC</div>
  <div class="front-rule"></div>
  <div class="front-doctor">Dr. Lorna Pettigrew</div>
  <ul class="contact-list">
    <li>
      <svg viewBox="0 0 18 14" aria-hidden="true"><path d="M4 1 L7 1 L8 4 L6.5 5.5 Q8 9 11 10.5 L12.5 9 L15 10 L15 13 Q6 13 4 1 Z" fill="#fff"/></svg>
      <span>610-555-0193</span>
    </li>
    <li>
      <svg viewBox="0 0 18 14" aria-hidden="true"><rect x="1" y="2" width="16" height="10" fill="none" stroke="#fff" stroke-width="1.6"/><path d="M1 2 L9 8 L17 2" fill="none" stroke="#fff" stroke-width="1.6"/></svg>
      <span>ferncrestdental.office@examplemail.test</span>
    </li>
    <li>
      <svg viewBox="0 0 18 14" aria-hidden="true"><path d="M9 1 L17 7 L15 7 L15 13 L11 13 L11 9 L7 9 L7 13 L3 13 L3 7 L1 7 Z" fill="#fff"/></svg>
      <span>2871 Marlowe Street<br>Bethlehem, PA 18093</span>
    </li>
  </ul>
</section>

<section class="card card-back" aria-label="Business card back">
  <div class="back-brand">
    <span class="brand-mark"></span>
    <span class="brand-name">Ferncrest Dental, LLC</span>
  </div>
  <svg class="back-band" viewBox="0 0 525 36" aria-hidden="true">
    <path d="M0 36 L70 4 Q77 1 86 1 L440 1 Q449 1 456 4 L525 36 Z" fill="var(--accent-blue)"/>
  </svg>
  <div class="back-doctor">Dr. Lorna Pettigrew</div>
</section>

</body>
</html>
```